Door Hanger for Bright Harbor Painters

Design a double-sided door hanger that reinforces Bright Harbor Painters’ brand identity while promoting our interior painting services. This piece will be distributed in residential neighborhoods during the winter and should make a strong visual impression at a glance while offering enough detail to motivate follow-up. See attached design brief.

```html
<!DOCTYPE html>
<html lang="en">
<head>
<meta charset="UTF-8">
<title>Bright Harbor Painters – Door Hanger</title>
<link href="https://fonts.googleapis.com/css2?family=Barlow+Condensed:wght@500&family=Barlow+Semi+Condensed:wght@500;600;700&family=Barlow:wght@400;500&display=swap" rel="stylesheet">
<style>
  :root {
    --brand-green: #145a3d;
    --ink-green: #17573b;
    --paper: #ffffff;
    --backdrop: #f3f3f3;
    --hole: #f1f1f1;
    --photo-light: #e4e8ec;
    --photo-mid: #c9d0d6;
  }
  * { margin: 0; padding: 0; box-sizing: border-box; }
  html, body { width: 800px; height: 1200px; overflow: hidden; background: var(--backdrop); }
  .canvas { position: relative; width: 800px; height: 1200px; }

  .hanger {
    position: absolute;
    top: 141px;
    width: 347px;
    height: 937px;
    border-radius: 24px;
    overflow: hidden;
  }
  .hanger-hole {
    position: absolute;
    left: 104px;
    top: 35px;
    width: 139px;
    height: 139px;
    border-radius: 50%;
    background: var(--hole);
  }
  .line { position: absolute; left: 0; width: 100%; text-align: center; white-space: nowrap; }

  /* Front */
  .hanger-front { left: 39px; background: var(--brand-green); color: var(--paper); }
  .headline {
    font-family: "Barlow Condensed", sans-serif;
    font-weight: 500;
    font-size: 102px;
    line-height: 1;
    letter-spacing: -1px;
  }
  .headline-interior { top: 196px; }
  .headline-painting { top: 283px; }
  .headline-season {
    top: 385px;
    font-family: "Barlow Semi Condensed", sans-serif;
    font-weight: 600;
    font-size: 46px;
    line-height: 1;
  }
  .photo-band {
    position: absolute;
    left: 0; top: 440px;
    width: 100%; height: 370px;
    background: linear-gradient(100deg, var(--photo-mid) 0%, var(--photo-light) 55%, #f5f6f7 100%);
    clip-path: polygon(0 36px, 100% 7px, 100% 332px, 0 364px);
  }
  .front-cta {
    font-family: "Barlow Semi Condensed", sans-serif;
    font-weight: 500;
    font-size: 36px;
    line-height: 43px;
    top: 840px;
  }

  /* Back */
  .hanger-back { left: 415px; background: var(--paper); color: var(--ink-green); }
  .hanger-back .hanger-hole { background: var(--hole); box-shadow: inset 0 1px 3px rgba(0,0,0,0.08); }
  .brand-dot {
    position: absolute;
    left: 144px; top: 232px;
    width: 58px; height: 58px;
    border-radius: 50%;
    background: var(--ink-green);
  }
  .brand-name {
    font-family: "Barlow Semi Condensed", sans-serif;
    font-weight: 700;
    font-size: 34px;
    line-height: 32px;
    letter-spacing: 0.5px;
  }
  .brand-name-top { top: 340px; }
  .brand-name-bottom { top: 372px; letter-spacing: 5px; font-size: 30px; }
  .tagline {
    top: 430px;
    font-family: "Barlow", sans-serif;
    font-weight: 400;
    font-size: 25px;
    line-height: 32px;
  }
  .offer-lead {
    top: 530px;
    font-family: "Barlow", sans-serif;
    font-weight: 400;
    font-size: 42px;
    line-height: 1;
  }
  .offer-main {
    font-family: "Barlow Semi Condensed", sans-serif;
    font-weight: 700;
    font-size: 62px;
    line-height: 1;
  }
  .offer-free { top: 586px; }
  .offer-estimate { top: 646px; }
  .phone {
    top: 739px;
    font-family: "Barlow Semi Condensed", sans-serif;
    font-weight: 700;
    font-size: 42px;
    line-height: 1;
  }
  .website {
    top: 790px;
    font-family: "Barlow", sans-serif;
    font-weight: 500;
    font-size: 17px;
    line-height: 1;
    color: #1d2b24;
  }
  .footer-band {
    position: absolute;
    left: 0; bottom: 0;
    width: 100%; height: 88px;
    background: var(--brand-green);
  }
</style>
</head>
<body>
<main class="canvas">

  <section class="hanger hanger-front" aria-label="Door hanger front">
    <div class="hanger-hole"></div>
    <div class="line headline headline-interior">INTERIOR</div>
    <div class="line headline headline-painting">PAINTING</div>
    <div class="line headline-season">THIS WINTER</div>
    <div class="photo-band" role="img" aria-label="Photo of a painter in a white cap rolling white paint beside a bright winter window"></div>
    <div class="line front-cta">Contact us for<br>a free estimate</div>
  </section>

  <section class="hanger hanger-back" aria-label="Door hanger back">
    <div class="hanger-hole"></div>
    <div class="brand-dot"></div>
    <div class="line brand-name brand-name-top">BRIGHT HARBOR</div>
    <div class="line brand-name brand-name-bottom">PAINTERS</div>
    <div class="line tagline">Professional, clean<br>and courteous service</div>
    <div class="line offer-lead">Call for a</div>
    <div class="line offer-main offer-free">FREE</div>
    <div class="line offer-main offer-estimate">ESTIMATE</div>
    <div class="line phone">802-555-0147</div>
    <div class="line website">www.brightharborpainters.com</div>
    <div class="footer-band"></div>
  </section>

</main>
</body>
</html>
```